Business Cards Design for the electrical wholesaler: clean bold dynamic :)

We need a business card design that would follow our latest brand guidelines. As an electrical wholesaler we want to bring a fresh look and feel into the industry. The design should be clean bold and dynamic. It should come alive with the renewed energy of our green colour. Our grey colour should keep things balanced and complement the notion of maturity and responsibility. We employ Lato as a corporate font however are not bound by this font and we’re open to interpretation here.

Target Market(s)

Electrical contractors

Industry/Entity Type

Business

Contact Information for Business Card

Logo
Name & Surname: Olena Dovbush
Job Title: Director of Marketing
Email: helen.dovbush@mailvane.example
Cell phone: XXX.XXX.XXXX
Address: 20917 - 87 Ave. Edmonton, AB, Canada. T6K 2R8
Business Phone: 780.555.0187
Website: www.qorvil.example

Font styles to use
Other font styles liked:
• Lato

Requirements
Must have
• Logo & website
Nice to have
• Brand elements - some of them you may find in the attached Brand Guidelines (e.g. three lines on the background signifying "W")

```html
<!DOCTYPE html>
<html lang="en">
<head>
<meta charset="utf-8">
<title>Business Cards</title>
<link href="https://fonts.googleapis.com/css2?family=Lato:wght@400;700&family=Open+Sans:ital,wght@1,700;1,800&family=Roboto+Condensed:wght@400;700&display=swap" rel="stylesheet">
<style>
  :root {
    --green: #78c04f;
    --charcoal: #2a2d28;
    --grey: #4d4e50;
    --card: #f4f5f5;
    --accent: #f5a623;
    --page: #ffffff;
    --white: #ffffff;
  }
  * { margin: 0; padding: 0; box-sizing: border-box; }
  html, body { width: 1200px; height: 1200px; overflow: hidden; background: var(--page); }
  .canvas { position: relative; width: 1200px; height: 1200px; }

  .card { position: absolute; left: 217px; width: 800px; height: 482px; background: var(--card); overflow: hidden; }
  .card--front { top: 50px; }
  .card--back { top: 634px; }

  .holder { position: absolute; left: 0; top: 130px; width: 425px; text-align: center; }
  .holder__name {
    font-family: "Open Sans", sans-serif; font-style: italic; font-weight: 800;
    font-size: 46px; line-height: 1.2; color: var(--charcoal); letter-spacing: -0.3px;
    white-space: nowrap;
  }
  .holder__title {
    margin-top: 2px; padding-left: 40px; white-space: nowrap;
    font-family: "Open Sans", sans-serif; font-style: italic; font-weight: 700;
    font-size: 18px; color: var(--green); letter-spacing: 0.3px;
  }

  .panel { position: absolute; left: 425px; top: 0; width: 375px; height: 482px; background: var(--green); }
  .panel__brand {
    position: absolute; left: 0; right: 0; top: 62px; text-align: center;
    font-family: "Lato", sans-serif; font-weight: 700; font-size: 82px; line-height: 1;
    color: var(--grey); letter-spacing: -1px;
  }

  .contact {
    position: absolute; left: 0; width: 375px; height: 68px; background: var(--charcoal);
    clip-path: polygon(0 0, 100% 0, 100% 100%, 0 100%, 23px 50%);
    display: flex; align-items: center;
  }
  .contact--address { top: 214px; }
  .contact--phone { top: 299px; }
  .contact--web { top: 384px; }
  .contact__icon { width: 34px; height: 34px; margin-left: 71px; flex: none; }
  .contact__text {
    margin-left: 22px; font-family: "Roboto Condensed", sans-serif; font-size: 15.5px;
    line-height: 19px; color: var(--white); white-space: nowrap; letter-spacing: -0.3px;
  }

  .lockup {
    position: absolute; left: 0; right: 0; top: 172px;
    display: flex; align-items: center; justify-content: center; gap: 26px;
  }
  .lockup__mark { width: 96px; height: 96px; border-radius: 50%; background: var(--green); flex: none; }
  .lockup__name {
    font-family: "Lato", sans-serif; font-weight: 700; font-size: 118px; line-height: 1;
    color: var(--grey); letter-spacing: -2px;
  }

  .footer-band {
    position: absolute; left: 0; bottom: 0; width: 100%; height: 66px; background: var(--green);
    display: flex; align-items: center; justify-content: center;
    font-family: "Roboto Condensed", sans-serif; font-weight: 700; font-size: 27px;
    color: var(--white); letter-spacing: 0.2px;
  }
</style>
</head>
<body>
<main class="canvas">

  <section class="card card--front">
    <div class="holder">
      <h1 class="holder__name">Olena Dovbush</h1>
      <p class="holder__title">DIRECTOR MARKETING</p>
    </div>

    <div class="panel">
      <div class="panel__brand">qorvil</div>

      <div class="contact contact--address">
        <svg class="contact__icon" viewBox="0 0 36 36" aria-hidden="true">
          <path d="M18 4 L2 18 L6 18 L6 32 L14 32 L14 23 L22 23 L22 32 L30 32 L30 18 L34 18 L28 12.7 L28 6 L24 6 L24 9.2 Z" fill="var(--accent)"/>
        </svg>
        <p class="contact__text">20917 - 87<br>Ave. Edmonton, AB, Canada. T6K 2R8</p>
      </div>

      <div class="contact contact--phone">
        <svg class="contact__icon" viewBox="0 0 36 36" aria-hidden="true">
          <path d="M9 4 L14 10 C15 11.5 14.5 13 13 14 L11.5 15 C13 19.5 16.5 23 21 24.5 L22 23 C23 21.5 24.5 21 26 22 L32 27 C33 28 32.5 29.5 31.5 30.5 L29.5 32 C27 34 20 32 13 25 C6 18 2 10 4 7 L6 4.5 C7 3.5 8.2 3.3 9 4 Z" fill="var(--accent)"/>
        </svg>
        <p class="contact__text">780.555.0187<br>XXX.XXX.XXXX</p>
      </div>

      <div class="contact contact--web">
        <svg class="contact__icon" viewBox="0 0 36 36" aria-hidden="true">
          <g fill="none" stroke="var(--accent)" stroke-width="2.4">
            <circle cx="18" cy="18" r="14"/>
            <ellipse cx="18" cy="18" rx="6.5" ry="14"/>
            <line x1="18" y1="4" x2="18" y2="32"/>
            <line x1="4" y1="18" x2="32" y2="18"/>
            <line x1="6.5" y1="10.5" x2="29.5" y2="10.5"/>
            <line x1="6.5" y1="25.5" x2="29.5" y2="25.5"/>
          </g>
        </svg>
        <p class="contact__text">WWW.QORVIL.EXAMPLE<br>helen.dovbush@mailvane.example</p>
      </div>
    </div>
  </section>

  <section class="card card--back">
    <div class="lockup">
      <span class="lockup__mark"></span>
      <span class="lockup__name">qorvil</span>
    </div>
    <div class="footer-band">WWW.QORVIL.EXAMPLE</div>
  </section>

</main>
</body>
</html>
```